Single page 8 1/2 x 11 flyer to entice new homeowners to visit our WEBSITE

A single page flyer that we can put on an easel that promotes our website, tallowpine58.com, to new homeowners for blinds, shades, bath hardware, cabinet organization, etc. This piece will be on an easel in sales centers, design studios and closing offices. We want the homeowners to know where they can go to get reliable products and service from a trusted partner of their builder for products that were not installed in their new home before they closed.

Enter the coupon code KQT10 to get 10% off of your entire purchase and free shipping. The product on our website will put the finishing touches on their home. ....make your house your home

Target Market(s)

New homebuyers

Industry/Entity Type

Residential Construction

Font styles to use
Serif

Colors
ec1f27

Requirements
Must have
• Logo and website, tallowpine58.com and tagline, make your house your home
Nice to have
• what will drive new homeowners to the website to purchase items they did not purchase before closing like window blinds and shades, bath hardware, ceiling fans, grills, electric fireplaces, etc.

```html
<!DOCTYPE html>
<html lang="en">
<head>
<meta charset="utf-8">
<title>Tallowpine 58 – Make Your House Your Home</title>
<link rel="stylesheet" href="https://fonts.googleapis.com/css2?family=Oswald:wght@300;400;500;600&family=Open+Sans:wght@400;600&display=swap">
<style>
  :root {
    --brand-red: #d21f26;
    --ink: #1d1d1d;
    --text-gray: #4a4a4a;
    --panel-gray: #e6e7e8;
    --badge-gray: #5d5e60;
    --rule-gray: #e3e4e5;
    --white: #ffffff;
  }
  * { box-sizing: border-box; margin: 0; padding: 0; }
  html, body { width: 989px; height: 1200px; overflow: hidden; background: var(--white); }
  .flyer { position: relative; width: 989px; height: 1200px; background: var(--white); font-family: "Open Sans", Arial, sans-serif; color: var(--text-gray); }

  .brand { position: absolute; left: 40px; top: 62px; display: flex; align-items: center; gap: 16px; }
  .brand-dot { width: 58px; height: 58px; border-radius: 50%; background: var(--brand-red); }
  .brand-name { font-family: "Oswald", sans-serif; font-weight: 500; font-size: 50px; line-height: 1; color: var(--ink); letter-spacing: 0.5px; }
  .brand-rule { position: absolute; left: 0; top: 183px; width: 512px; height: 6px; background: var(--brand-red); }

  .offer-panel { position: absolute; left: 0; top: 189px; width: 512px; height: 294px; background: var(--panel-gray); }
  .tagline { position: absolute; left: 40px; top: 216px; font-family: "Oswald", sans-serif; font-weight: 500; font-size: 58px; line-height: 62px; color: var(--brand-red); text-transform: uppercase; }
  .discount { position: absolute; left: 38px; top: 360px; display: flex; align-items: baseline; gap: 8px; }
  .discount-amount { font-family: "Oswald", sans-serif; font-weight: 500; font-size: 56px; line-height: 1; color: var(--ink); letter-spacing: -1px; }
  .discount-note { font-size: 22px; color: var(--ink); }
  .promo-hint { position: absolute; left: 40px; top: 428px; font-size: 17px; color: var(--text-gray); }
  .shipping-bar { position: absolute; left: 0; top: 483px; width: 456px; height: 54px; background: var(--brand-red); color: var(--white); font-family: "Oswald", sans-serif; font-weight: 300; font-size: 23px; letter-spacing: 1.5px; line-height: 54px; padding-left: 38px; white-space: nowrap; }

  .hero-photo { position: absolute; left: 512px; top: 0; width: 477px; height: 537px; background: linear-gradient(135deg, #9a948c 0%, #cfcac3 45%, #eeece8 75%, #d9d2c8 100%); }

  .product-photo { position: absolute; width: 223px; height: 219px; border: 1px solid #d8d8d8; }
  .photo-shelving { left: 40px; top: 605px; background: linear-gradient(160deg, #d8d2c6, #f1eee9 55%, #6f7278); }
  .photo-pantry { left: 290px; top: 605px; background: linear-gradient(170deg, #c9ccd0, #8f959c 55%, #d9b98c); }
  .photo-living { left: 40px; top: 846px; background: linear-gradient(180deg, #f2ede3, #e6e0d4 60%, #b7b79a); }
  .photo-grill { left: 290px; top: 846px; background: linear-gradient(150deg, #7fc8c4, #7a7d80 45%, #c0c3c6 80%, #c45a3c); }

  .intro { position: absolute; left: 560px; top: 600px; width: 394px; font-size: 18.5px; line-height: 25px; text-align: justify; color: var(--text-gray); }
  .intro p + p { margin-top: 24px; }
  .intro .accent { color: var(--brand-red); }

  .benefit-box { position: absolute; left: 698px; top: 935px; width: 256px; height: 111px; background: var(--badge-gray); border-radius: 0 4px 4px 0; padding: 12px 0 0 62px; }
  .benefit-list { list-style: none; }
  .benefit-list li { display: flex; align-items: center; gap: 14px; height: 31px; font-family: "Oswald", sans-serif; font-weight: 400; font-size: 21px; letter-spacing: 2px; color: var(--white); margin-left: -26px; }
  .benefit-list svg { width: 16px; height: 16px; flex: none; }

  .badge-ring { position: absolute; left: 571px; top: 921px; width: 146px; height: 146px; border-radius: 50%; background: var(--white); }
  .badge-core { position: absolute; left: 579px; top: 929px; width: 130px; height: 130px; border-radius: 50%; border: 5px solid var(--brand-red); background: var(--white); text-align: center; padding-top: 22px; }
  .badge-amount { font-family: "Oswald", sans-serif; font-weight: 500; font-size: 40px; line-height: 40px; color: var(--brand-red); }
  .badge-amount small { font-size: 26px; }
  .badge-note { font-size: 14px; line-height: 15px; color: var(--text-gray); }

  .footer-rule { position: absolute; left: 0; top: 1095px; width: 989px; height: 9px; background: var(--rule-gray); }
  .contact-bar { position: absolute; left: 0; top: 1104px; width: 989px; height: 96px; background: var(--brand-red); display: flex; align-items: center; justify-content: space-between; padding: 0 40px; color: var(--white); font-size: 22px; }
  .contact-item { display: flex; align-items: center; gap: 10px; }
  .contact-item svg { width: 22px; height: 22px; }
</style>
</head>
<body>
<main class="flyer">
  <header>
    <div class="brand">
      <span class="brand-dot"></span>
      <span class="brand-name">TALLOWPINE 58</span>
    </div>
    <div class="brand-rule"></div>
  </header>

  <section class="offer">
    <div class="offer-panel"></div>
    <h1 class="tagline">Make your<br>house your home</h1>
    <div class="discount">
      <span class="discount-amount">10% OFF</span>
      <span class="discount-note">your entire purchase!</span>
    </div>
    <p class="promo-hint">use promo code KQT10</p>
    <div class="shipping-bar">FREE SHIPPING ON EVERYTHING</div>
  </section>

  <div class="hero-photo" role="img" aria-label="Living room corner with a white wingback armchair, ottoman, wooden side table and lamp against a reclaimed wood wall"></div>

  <div class="product-photo photo-shelving" role="img" aria-label="Bright living room with built-in shelving and window blinds"></div>
  <div class="product-photo photo-pantry" role="img" aria-label="Grey kitchen with pull-out pantry cabinet organization"></div>
  <div class="product-photo photo-living" role="img" aria-label="Living room with ceiling fan and window shades"></div>
  <div class="product-photo photo-grill" role="img" aria-label="Stainless outdoor grill with food beside a pool"></div>

  <section class="intro">
    <p>Your builder and their trusted suppliers have partnered together to offer you this special opportunity.</p>
    <p>Go to <span class="accent">www.tallowpine58.com</span> and shop for your window coverings, ceiling fans, cabinet and closet organization, bath hardware and more.</p>
    <p>During Checkout, enter promo code <span class="accent">KQT10</span> and get a <span class="accent">10% discount</span> on your entire purchase!</p>
  </section>

  <aside class="benefits">
    <div class="benefit-box">
      <ul class="benefit-list">
        <li><svg viewBox="0 0 16 16"><rect x="1" y="3" width="11" height="11" fill="none" stroke="#fff" stroke-width="1.5"/><path d="M4 8l3 3 8-9" fill="none" stroke="#fff" stroke-width="1.8"/></svg>COMFORT</li>
        <li><svg viewBox="0 0 16 16"><rect x="1" y="3" width="11" height="11" fill="none" stroke="#fff" stroke-width="1.5"/><path d="M4 8l3 3 8-9" fill="none" stroke="#fff" stroke-width="1.8"/></svg>FUNCTIONALITY</li>
        <li><svg viewBox="0 0 16 16"><rect x="1" y="3" width="11" height="11" fill="none" stroke="#fff" stroke-width="1.5"/><path d="M4 8l3 3 8-9" fill="none" stroke="#fff" stroke-width="1.8"/></svg>UPGRADE</li>
      </ul>
    </div>
    <div class="badge-ring"></div>
    <div class="badge-core">
      <div class="badge-amount">10%<small>off</small></div>
      <div class="badge-note">with your<br>builder code</div>
    </div>
  </aside>

  <div class="footer-rule"></div>
  <footer class="contact-bar">
    <span class="contact-item">
      <svg viewBox="0 0 22 22"><path d="M2 9l9-6 9 6v10H2z" fill="none" stroke="#fff" stroke-width="1.8"/><path d="M2 9l9 6 9-6" fill="none" stroke="#fff" stroke-width="1.8"/></svg>
      support@tallowpine58.com
    </span>
    <span class="contact-item">
      <svg viewBox="0 0 22 22"><circle cx="11" cy="11" r="9" fill="none" stroke="#fff" stroke-width="1.6"/><ellipse cx="11" cy="11" rx="4" ry="9" fill="none" stroke="#fff" stroke-width="1.4"/><path d="M2 11h18M4 6h14M4 16h14" stroke="#fff" stroke-width="1.3"/></svg>
      www.tallowpine58.com
    </span>
    <span class="contact-item">
      <svg viewBox="0 0 22 22"><path d="M2 8c0-3 4-5 9-5s9 2 9 5l-3 1-1-2H6L5 9z" fill="#fff"/><path d="M6 10h10l3 9H3z" fill="#fff"/><circle cx="11" cy="14" r="2.2" fill="#d21f26"/></svg>
      (555) 014-2270
    </span>
  </footer>
</main>
</body>
</html>
```